Birch Endodontics business stationary
stationary, envelopes, business cards, referral pad, digital signature for email
Professional
R. Marlowe Birch, DDS, MS
2267 Orchard Crest Dr
Monroe, NC 28471
toothcare@birchendo-example.com
www.birchendo-example.com
I'm going to upload a couple of sample referral pads from other endodontic offices. Please refer to these for a template. I will also upload a couple of maps. I need a simple map drawn to find the office. Voxmap address is wrong. I will mark the location on the map I upload. The fax number I listed will be changed in a couple days so I will update with the correct number.
I need the back to be a place where the patient's appointment date and time can be recorded.
This is the logo to be used.
Please reference these to draw a simple map on the back of the referral pad
map
sample referral pad
I like the style of this pad alot.
I like this referral pad
I sketched how the map should look.
I sketched the layout for the referral pad.

```html
<!DOCTYPE html>
<html lang="en">
<head>
<meta charset="utf-8">
<title>Birch Endodontics Stationery</title>
<link href="https://fonts.googleapis.com/css2?family=Nunito:wght@400;700;800&display=swap" rel="stylesheet">
<style>
:root{
  --blue:#1ba3dc;
  --blue-dark:#0c7fb8;
  --green:#8dc63f;
  --green-dark:#6aa628;
  --paper:#ffffff;
  --ink:#4a4f55;
  --muted:#8c949c;
  --stage:#eef0f2;
  --shadow:0 3px 10px rgba(0,0,0,.18);
}
*{box-sizing:border-box;margin:0;padding:0}
html,body{width:1200px;height:588px;overflow:hidden}
body{background:var(--stage);font-family:'Nunito',sans-serif;color:var(--ink);position:relative}
.brand{display:flex;align-items:center;gap:5px}
.brand-dot{border-radius:50%;background:var(--green);flex:none}
.brand-name{font-weight:800;color:var(--blue);white-space:nowrap}

/* business cards */
.card{position:absolute;width:150px;height:88px;border-radius:4px;box-shadow:var(--shadow);overflow:hidden;background:var(--paper)}
.card .brand{position:absolute}
.card-front .brand{left:10px;top:10px}
.card-front .brand-dot{width:12px;height:12px}
.card-front .brand-name{font-size:10px}
.card-front .details{position:absolute;left:10px;bottom:9px;font-size:5.5px;line-height:1.45;color:var(--muted)}
.card-front .details strong{color:var(--ink);font-size:6.5px}
.card-info .details{left:auto;right:10px;text-align:right;top:12px;bottom:auto}
.card-info .brand{top:auto;bottom:10px}
.card-color .brand{left:50%;top:18px;transform:translateX(-50%)}
.card-color .brand-dot{width:12px;height:12px;background:#fff}
.card-color .brand-name{font-size:10px;color:#fff}
.card-green{background:linear-gradient(160deg,var(--green),var(--green-dark))}
.card-blue{background:linear-gradient(160deg,var(--blue),var(--blue-dark))}
.card-color .tagline{position:absolute;left:0;right:0;top:40px;text-align:center;font-size:6px;color:#fff}
.appt{position:absolute;left:12px;right:12px;top:40px;font-size:6px;color:#fff;line-height:2}
.appt span{display:block;border-bottom:1px solid rgba(255,255,255,.7)}
.card-wave{position:absolute;left:0;bottom:0;width:100%;height:22px}

/* letterhead */
.sheet{position:absolute;width:290px;height:420px;background:var(--paper);box-shadow:var(--shadow)}
.sheet-back{left:424px;top:88px}
.sheet-front{left:408px;top:72px}
.sheet-front .brand{position:absolute;left:22px;top:24px}
.sheet-front .brand-dot{width:18px;height:18px}
.sheet-front .brand-name{font-size:15px}
.sheet-contact{position:absolute;left:22px;top:58px;font-size:6.5px;line-height:1.5;color:var(--muted)}
.sheet-wave{position:absolute;left:0;bottom:0;width:100%;height:60px}
.sheet-web{position:absolute;right:14px;bottom:8px;font-size:6.5px;color:#fff}

/* envelopes */
.envelope{position:absolute;width:350px;height:170px;background:var(--paper);box-shadow:var(--shadow);overflow:hidden}
.envelope-back{left:790px;top:96px}
.envelope-back svg{position:absolute;inset:0;width:100%;height:100%}
.envelope-back .flap-mark{position:absolute;left:50%;top:34px;transform:translateX(-50%);width:22px;height:22px;border-radius:50%;background:#fff}
.envelope-front{left:760px;top:300px}
.envelope-front .brand{position:absolute;left:16px;top:16px}
.envelope-front .brand-dot{width:14px;height:14px}
.envelope-front .brand-name{font-size:12px}
.envelope-front .return{position:absolute;left:16px;top:40px;font-size:6px;color:var(--muted)}
.envelope-front .env-wave{position:absolute;left:0;bottom:0;width:100%;height:40px}
</style>
</head>
<body>

<!-- business cards -->
<div class="card card-front" style="left:40px;top:130px">
  <div class="brand"><span class="brand-dot"></span><span class="brand-name">Birch Endodontics</span></div>
  <div class="details"><strong>R. Marlowe Birch, DDS, MS</strong><br>2267 Orchard Crest Dr, Monroe, NC 28471</div>
</div>
<div class="card card-front card-info" style="left:200px;top:130px">
  <div class="details"><strong>R. Marlowe Birch, DDS, MS</strong><br>2267 Orchard Crest Dr<br>Monroe, NC 28471<br>Phone 704-555-0182<br>toothcare@birchendo-example.com</div>
  <div class="brand"><span class="brand-dot"></span><span class="brand-name">Birch Endodontics</span></div>
</div>

<div class="card card-color card-green" style="left:40px;top:232px">
  <div class="brand"><span class="brand-dot"></span><span class="brand-name">Birch Endodontics</span></div>
  <div class="tagline">Gentle care for healthy roots</div>
  <svg class="card-wave" viewBox="0 0 150 22" preserveAspectRatio="none"><path d="M0 14 C40 2 90 26 150 8 V22 H0Z" fill="rgba(255,255,255,.25)"/></svg>
</div>
<div class="card card-color card-blue" style="left:200px;top:232px">
  <div class="brand"><span class="brand-dot"></span><span class="brand-name">Birch Endodontics</span></div>
  <div class="tagline">www.birchendo-example.com</div>
  <svg class="card-wave" viewBox="0 0 150 22" preserveAspectRatio="none"><path d="M0 14 C40 2 90 26 150 8 V22 H0Z" fill="rgba(255,255,255,.25)"/></svg>
</div>

<div class="card card-color card-green" style="left:40px;top:334px">
  <div class="brand" style="top:10px"><span class="brand-dot"></span><span class="brand-name">Birch Endodontics</span></div>
  <div class="appt"><span>Appointment date:</span><span>Time:</span></div>
</div>
<div class="card card-color card-blue" style="left:200px;top:334px">
  <div class="brand" style="top:10px"><span class="brand-dot"></span><span class="brand-name">Birch Endodontics</span></div>
  <div class="appt"><span>Appointment date:</span><span>Time:</span></div>
</div>

<!-- letterhead -->
<div class="sheet sheet-back"></div>
<div class="sheet sheet-front">
  <div class="brand"><span class="brand-dot"></span><span class="brand-name">Birch Endodontics</span></div>
  <div class="sheet-contact">2267 Orchard Crest Dr, Monroe, NC 28471<br>Phone: 704-555-0182 | Fax: 704-555-0190<br>Email: toothcare@birchendo-example.com</div>
  <svg class="sheet-wave" viewBox="0 0 290 60" preserveAspectRatio="none">
    <path d="M0 30 C90 10 180 50 290 20 V60 H0Z" fill="var(--green)"/>
    <path d="M0 40 C100 22 190 58 290 32 V60 H0Z" fill="var(--blue)"/>
  </svg>
  <div class="sheet-web">www.birchendo-example.com</div>
</div>

<!-- envelopes -->
<div class="envelope envelope-back">
  <svg viewBox="0 0 350 170" preserveAspectRatio="none">
    <path d="M0 0 H350 L190 88 Q175 96 160 88 Z" fill="var(--blue)"/>
    <path d="M0 0 L160 88 Q175 96 190 88 L350 0" fill="none" stroke="var(--blue-dark)" stroke-width="1"/>
    <path d="M0 170 L150 92 M350 170 L200 92" stroke="#dde2e6" stroke-width="1"/>
  </svg>
  <div class="flap-mark"></div>
</div>
<div class="envelope envelope-front">
  <div class="brand"><span class="brand-dot"></span><span class="brand-name">Birch Endodontics</span></div>
  <div class="return">2267 Orchard Crest Dr, Monroe, NC 28471</div>
  <svg class="env-wave" viewBox="0 0 350 40" preserveAspectRatio="none">
    <path d="M0 22 C110 4 220 36 350 12 V40 H0Z" fill="var(--green)"/>
    <path d="M0 30 C120 14 230 42 350 22 V40 H0Z" fill="var(--blue)"/>
  </svg>
</div>

</body>
</html>
```